Business Card for Lawyer

I'm looking for a business card for my new law firm, based in Ontario, Canada. I would prefer single sided. I am partial (but not limited) to white and blue color wise and like things understated. Also, if you can work in the red QK rating symbol from Presworth-Calloway, that would be a plus.

Target Market(s)

Old people - so it should be easy to read.

Industry/Entity Type

Business

Contact Information for Business Card

See the specs in the word document below. Also, see the design for my website. The card should have a similar look to the site.

Requirements
Must have
• Everything listed in the business card specs. I don't mind having the address set off at the bottom of the card on its own line.
Should not have
• 1) Any sort of design that could also be used by a tattoo parlour or a tarot card reader, mystic etc.
• 2) There should not be any photographs of me (or anyone else).

```html
<!DOCTYPE html>
<html lang="en">
<head>
<meta charset="utf-8">
<title>Halden's Law Firm – Business Card</title>
<link rel="stylesheet" href="https://fonts.googleapis.com/css2?family=Tinos:ital,wght@0,400;1,400&display=swap">
<style>
  :root {
    --page-bg: #ece9e4;
    --brown-deep: #2e1a0e;
    --brown: #4a2c17;
    --brown-warm: #5a3720;
    --cream: #f7f2ea;
    --white: #ffffff;
    --paper-edge: #e6e6e6;
    --ink: #1e1e1e;
    --ink-soft: #555555;
    --red: #d7464f;
    --red-dot: #e0242f;
  }
  * { box-sizing: border-box; margin: 0; padding: 0; }
  html, body { width: 1200px; height: 858px; overflow: hidden; }
  body {
    background: var(--page-bg);
    font-family: "Tinos", "Times New Roman", serif;
    display: flex;
    align-items: center;
    justify-content: center;
    gap: 60px;
  }
  .card {
    position: relative;
    width: 525px;
    height: 300px;
    border-radius: 3px;
    box-shadow: 0 10px 28px rgba(0,0,0,.22);
    overflow: hidden;
  }

  /* Front */
  .card--front {
    background: linear-gradient(135deg, var(--brown-warm) 0%, var(--brown) 50%, var(--brown-deep) 100%);
    color: var(--cream);
  }
  .card__art {
    position: absolute;
    top: 0; right: 0;
    width: 215px; height: 300px;
    background: radial-gradient(ellipse at 55% 60%, #6e3b22 0%, #4a2a17 45%, rgba(46,26,14,0) 80%);
  }
  .firm-name {
    position: absolute;
    left: 34px; top: 36px;
    font-size: 40px;
    letter-spacing: .5px;
    line-height: 1;
  }
  .tagline {
    position: absolute;
    left: 36px; top: 84px;
    font-size: 15px;
  }
  .lawyer {
    position: absolute;
    left: 60px; top: 124px;
    font-size: 18px;
    line-height: 1.35;
  }
  .contacts {
    position: absolute;
    left: 60px; top: 192px;
    list-style: none;
    font-size: 15px;
    line-height: 22px;
  }
  .contacts li { display: flex; align-items: center; gap: 12px; }
  .contacts svg { width: 13px; height: 13px; fill: var(--cream); flex: none; }

  /* Back */
  .card--back {
    background: linear-gradient(160deg, var(--white) 0%, #f4f4f4 60%, var(--paper-edge) 100%);
    color: var(--ink);
  }
  .rating-badge {
    position: absolute;
    left: 0; top: 22px;
    width: 180px; height: 34px;
    background: var(--red);
  }
  .rating-source {
    position: absolute;
    left: 14px; top: 62px;
    font-size: 13px;
    font-style: italic;
    color: var(--ink-soft);
  }
  .services {
    position: absolute;
    left: 255px; top: 120px;
    list-style: none;
    font-size: 18px;
    line-height: 23px;
  }
  .services li { display: flex; align-items: center; gap: 10px; }
  .services li::before {
    content: "";
    width: 7px; height: 7px;
    border-radius: 50%;
    background: var(--red-dot);
    flex: none;
  }
  .address {
    position: absolute;
    left: 235px; top: 240px;
    display: flex;
    gap: 8px;
    color: var(--red);
    font-size: 15px;
    line-height: 19px;
  }
  .address svg { width: 10px; height: 13px; margin-top: 2px; fill: none; stroke: var(--ink); stroke-width: 1.6; flex: none; }
</style>
</head>
<body>

<section class="card card--front" aria-label="Business card front">
  <div class="card__art" role="img" aria-label="Photograph of scales of justice and a wooden gavel"></div>
  <h1 class="firm-name">Halden's Law Firm</h1>
  <p class="tagline">"Getting the results that matter"</p>
  <p class="lawyer">Halden R. Voss<br>B.A. &amp; J.D</p>
  <ul class="contacts">
    <li>
      <svg viewBox="0 0 16 16" aria-hidden="true"><path d="M4 1l3 3-2 2c1 2 3 4 5 5l2-2 3 3-2 3C7 15 1 9 1 3z"/></svg>
      555.210.xxxx
    </li>
    <li>
      <svg viewBox="0 0 16 16" aria-hidden="true"><rect x="4" y="1" width="8" height="5"/><rect x="1" y="6" width="14" height="6"/><rect x="4" y="11" width="8" height="4"/></svg>
      555.318.xxxx
    </li>
    <li>
      <svg viewBox="0 0 16 16" aria-hidden="true"><path d="M1 3h14v10H1z M1 3l7 6 7-6" stroke="#4a2c17" stroke-width="1"/></svg>
      www.haldensfirm.ca
    </li>
    <li>
      <svg viewBox="0 0 16 16" aria-hidden="true"><circle cx="8" cy="8" r="7"/><path d="M1 8h14M8 1c-3 3-3 11 0 14M8 1c3 3 3 11 0 14" stroke="#4a2c17" stroke-width="1" fill="none"/></svg>
      xxxx@haldensfirm.ca
    </li>
  </ul>
</section>

<section class="card card--back" aria-label="Business card back">
  <div class="rating-badge" aria-hidden="true"></div>
  <p class="rating-source">Presworth-Calloway</p>
  <ul class="services">
    <li>Barrister</li>
    <li>Solicitor &amp; Notary Public</li>
    <li>Lawyer</li>
    <li>Litigation Counsel</li>
    <li>Trial Lawyer</li>
  </ul>
  <div class="address">
    <svg viewBox="0 0 10 13" aria-hidden="true"><path d="M5 12C2 8 1 6 1 4.5a4 4 0 0 1 8 0C9 6 8 8 5 12z"/><circle cx="5" cy="4.5" r="1.3"/></svg>
    <p>48 Ferrow Lane West, Ground Floor<br>Ashbury, ON K0X 9Z9</p>
  </div>
</section>

</body>
</html>
```